Compatible Printer Cartridge Box Design

We are looking to package toners cartridges & ink cartridges that we recycle in our shop. Attached is a doc file that tell what design we want, ideas, and sizes.

Unlike other compatible toner cartridges that are manufactured from scratch, LUMO Print Consumables are made from recycled original OEM print toners. This will maintain the original OEM parts inside the cartridge, maintain the original cartridge tolerance, ensure proper cartridge alignment in the printer, and minimize human error.

Project Deadline Extended
Reason: Hi to all, I am not satisfied with the current designs. I will extend for more 5 days and increase the budget. Thank You

Target Market(s)

Construction Companies, Banks, Hospitals, Oil Companies, Insurance Companies

Industry/Entity Type

Printer

Font styles to use
Other font styles liked:
• Calibri

Requirements
Must have
• The file must be in .ai format. So we can change the size of the box any time later.
• The file must be ready to be given to the printing press (specially the die cut). No any alteration must be made from our side.
• Since there are different models of cartridges, one side of the box must be left for a label that state the cartridge model, bar code, and compatible printers.
• The theme of the box must be quoted from our company logo, specially the colors. We prefer bold corporate design. Maybe with a woman on it (Not a must), and something related to protecting the environment. Avoid using the carton brown color.
• We prefer toner box that Can be opened from the top with that cartoon lock. For the ink cartridge, we would like to look like the zx one.
Nice to have
• Maybe with a woman on it (Not a must), and something related to protecting the environment.
Should not have
• Avoid using the carton brown color.

```html
<!DOCTYPE html>
<html lang="en">
<head>
<meta charset="utf-8">
<title>LUMO Premium Toner – Box Panels</title>
<link href="https://fonts.googleapis.com/css2?family=Oswald:wght@300;400;500;600&display=swap" rel="stylesheet">
<style>
  :root {
    --bg: #e6ebef;
    --panel: #fbfbfb;
    --side: #e4f0fb;
    --orange: #dd8a22;
    --ink-dark: #1f1f1f;
    --ink-grey: #4a4a4a;
    --label: #3a3a3a;
    --brand-green: #6f9a2c;
    --band: #1a1a1a;
    --band-text: #ffffff;
  }
  * { margin: 0; padding: 0; box-sizing: border-box; }
  html, body { width: 1200px; height: 675px; overflow: hidden; }
  body {
    background: var(--bg);
    font-family: "Oswald", "Arial Narrow", sans-serif;
    position: relative;
  }
  .box-front, .box-end {
    position: absolute;
    top: 190px;
    height: 290px;
    box-shadow: 0 6px 18px rgba(0,0,0,0.12);
  }
  .box-front {
    left: 60px;
    width: 840px;
    background: var(--panel);
  }
  .box-end {
    left: 900px;
    width: 240px;
    background: var(--side);
  }
  .hero-photo {
    position: absolute;
    left: 0; top: 0;
    width: 160px; height: 290px;
    background: radial-gradient(circle at 45% 35%, #f2c6a8 0%, #e8a98a 30%, #f3f3f3 70%),
                linear-gradient(135deg, #ff4fa0, #ffd23a, #40c6ff);
    background-blend-mode: multiply;
  }
  .headline {
    position: absolute;
    left: 180px; top: 22px;
    font-size: 68px;
    font-weight: 500;
    letter-spacing: 1px;
    line-height: 1;
    color: var(--ink-grey);
    white-space: nowrap;
  }
  .headline .accent { color: var(--ink-dark); font-weight: 600; }
  .features {
    position: absolute;
    left: 178px; top: 138px;
    display: flex;
    gap: 10px;
    list-style: none;
  }
  .feature {
    width: 78px;
    display: flex;
    flex-direction: column;
    align-items: center;
    text-align: center;
  }
  .feature-badge {
    width: 62px; height: 62px;
    border-radius: 50%;
    background: var(--orange);
    display: flex; align-items: center; justify-content: center;
  }
  .feature-badge .inner {
    width: 34px; height: 34px;
    border-radius: 50%;
    border: 3px solid #fff;
  }
  .feature-label {
    margin-top: 14px;
    font-size: 10px;
    font-weight: 300;
    line-height: 1.15;
    text-transform: uppercase;
    color: var(--label);
  }
  .brand-mark {
    position: absolute;
    display: flex;
    align-items: center;
    gap: 8px;
  }
  .brand-mark .square {
    background: var(--orange);
  }
  .brand-mark .name {
    font-weight: 600;
    color: var(--brand-green);
    letter-spacing: 0.5px;
  }
  .brand-front { left: 640px; top: 150px; }
  .brand-front .square { width: 70px; height: 70px; }
  .brand-front .name { font-size: 30px; }
  .brand-end {
    left: 0; right: 0; top: 55px;
    flex-direction: column;
    gap: 10px;
  }
  .brand-end .square { width: 80px; height: 80px; }
  .brand-end .name { font-size: 30px; }
  .recycle-band {
    position: absolute;
    left: 0; right: 0; top: 212px;
    height: 34px;
    background: var(--band);
    color: var(--band-text);
    font-size: 14px;
    font-weight: 400;
    letter-spacing: 0.5px;
    display: flex; align-items: center; justify-content: center;
    white-space: nowrap;
  }
</style>
</head>
<body>
  <section class="box-front">
    <div class="hero-photo" role="img" aria-label="Photo of a woman with rainbow-coloured hair and colourful beads on a white background with coloured dots"></div>

    <h1 class="headline">LUMO <span class="accent">PREMIUM</span> TONER</h1>

    <ul class="features">
      <li class="feature">
        <div class="feature-badge"><div class="inner"></div></div>
        <p class="feature-label">3 Years<br>Warranty</p>
      </li>
      <li class="feature">
        <div class="feature-badge"><div class="inner"></div></div>
        <p class="feature-label">Made in UAE</p>
      </li>
      <li class="feature">
        <div class="feature-badge"><div class="inner"></div></div>
        <p class="feature-label">ISO 19752<br>Certified Yield</p>
      </li>
      <li class="feature">
        <div class="feature-badge"><div class="inner"></div></div>
        <p class="feature-label">Guaranteed</p>
      </li>
      <li class="feature">
        <div class="feature-badge">
          <svg width="34" height="34" viewBox="0 0 34 34" aria-hidden="true">
            <circle cx="17" cy="17" r="15" fill="none" stroke="#fff" stroke-width="3"/>
            <path d="M10 17.5 L15 22.5 L24 12" fill="none" stroke="#fff" stroke-width="3.5" stroke-linecap="round" stroke-linejoin="round"/>
          </svg>
        </div>
        <p class="feature-label">STMC Compliant<br>Product</p>
      </li>
    </ul>

    <div class="brand-mark brand-front">
      <span class="square"></span>
      <span class="name">Lumova</span>
    </div>
  </section>

  <section class="box-end">
    <div class="brand-mark brand-end">
      <span class="square"></span>
      <span class="name">Lumova</span>
    </div>
    <div class="recycle-band">RECYCLE TODAY FOR BETTER TOMORROW</div>
  </section>
</body>
</html>
```